Packaging for a new tea company

Hi guys we need a new packaging design for a tea company we are starting

Our competitors are leafora, zip an brew

I have uploaded pictures of our competitors for you to see the sample
The label need to be catchy

Our brand is called #JoinVividLeaf
We need two packaging designs one for Zest Brew and one for calmora

Detox - slim - cleanse

Also needs to says 14 Day Brewreset

Target Market(s)

Young people

Industry/Entity Type

It Company

Colors
000000

Requirements
Must have
• #joinvividleaf
Nice to have
• Herbal tea supplement 50gram
• Max label size 13.5cm x 16.5 cm
• Personally I like the paper brown bag as it looks like a higher quality and as the label is a sticker I think this would make the product look a lot better
Should not have
• Nothing

```html
<!DOCTYPE html>
<html lang="en">
<head>
<meta charset="utf-8">
<title>JoinVividLeaf – 14 Days Brewreset label</title>
<link href="https://fonts.googleapis.com/css2?family=Roboto:wght@700;900&display=swap" rel="stylesheet">
<style>
  :root {
    --stage: #ededed;
    --leaf-dark: #1f3a1c;
    --leaf-mid: #3f7a32;
    --leaf-light: #6fae4a;
    --brand-green: #0f9a3c;
    --brand-yellow: #ffde00;
    --ink-dark: #222222;
    --badge-white: #ffffff;
    --text-green: #11802f;
  }
  * { margin: 0; padding: 0; box-sizing: border-box; }
  html, body { width: 1200px; height: 901px; overflow: hidden; background: var(--stage); }
  .canvas { position: relative; width: 1200px; height: 901px; }
  .label {
    position: absolute; left: 340px; top: 100px; width: 520px; height: 700px;
    overflow: hidden; font-family: "Roboto", Arial, sans-serif; font-weight: 700;
  }
  .label-art { position: absolute; inset: 0; }
  .leaf-photo { position: absolute; inset: 0;
    background: linear-gradient(160deg, var(--leaf-light) 0%, var(--leaf-mid) 45%, var(--leaf-dark) 100%); }
  .brand-band {
    position: absolute; left: 0; top: 40px; width: 100%; height: 56px;
    background: var(--brand-yellow); display: flex; align-items: center; justify-content: center;
  }
  .brand-name { color: var(--text-green); font-size: 36px; font-weight: 700; letter-spacing: 0.5px; }
  .claim-badge {
    position: absolute; left: 36px; top: 120px; width: 128px; height: 128px; border-radius: 50%;
    background: var(--badge-white); display: flex; flex-direction: column; align-items: center; justify-content: center;
    color: var(--text-green); font-size: 19px; line-height: 1.05; text-align: center; transform: rotate(-8deg);
  }
  .headline { position: absolute; left: 0; width: 100%; color: var(--brand-yellow); font-weight: 900; line-height: 1; }
  .headline-number { top: 128px; left: 200px; width: auto; font-size: 190px; letter-spacing: -4px; }
  .headline-days { top: 330px; text-align: center; padding-left: 60px; font-size: 92px; }
  .headline-product { top: 430px; text-align: center; padding-left: 20px; font-size: 70px; letter-spacing: -1px; }
  .promise-band {
    position: absolute; left: 0; top: 572px; width: 100%; height: 40px; background: var(--brand-yellow);
    display: flex; align-items: center; justify-content: center; color: var(--text-green); font-size: 20px;
  }
  .promise-rule { position: absolute; left: 0; width: 100%; height: 4px; background: var(--brand-yellow); }
  .variant-tab {
    position: absolute; left: 185px; top: 626px; width: 150px; height: 28px; background: var(--brand-yellow);
    border-radius: 0 0 6px 6px; display: flex; align-items: center; justify-content: center;
    color: var(--text-green); font-size: 14px; letter-spacing: 0.5px;
  }
</style>
</head>
<body>
<main class="canvas">
  <section class="label">
    <div class="leaf-photo" role="img" aria-label="Close-up photo of fresh green tea leaves"></div>
    <svg class="label-art" width="520" height="700" viewBox="0 0 520 700" aria-hidden="true">
      <polygon class="shade-panel" points="0,96 520,96 520,250 0,450" fill="var(--ink-dark)" opacity="0.92"/>
      <polygon class="diagonal-band" points="0,450 520,250 520,572 0,572" fill="var(--brand-green)"/>
    </svg>
    <div class="brand-band"><span class="brand-name">JoinVividLeaf</span></div>
    <div class="claim-badge"><span>DETOX</span><span>SLIM</span><span>CLEANSE</span></div>
    <div class="headline headline-number">14</div>
    <div class="headline headline-days">DAYS</div>
    <div class="headline headline-product">BREWRESET</div>
    <div class="promise-rule" style="top:562px"></div>
    <div class="promise-band">100 % Natural and Preservative FREE</div>
    <div class="promise-rule" style="top:616px"></div>
    <div class="variant-tab">ZEST BREW</div>
  </section>
</main>
</body>
</html>
```